Flyer informing about the activities of people in action

Wege im Wandel (www.wegeimwandel-beratung.ch) offers coaching, medation, support for traumatized people and conflict and crisis intervention. The flyer should inform about the activities in a plain and simple way (see logo on the homepage).

Target Market(s)

Adults who live in Switzerland or Germany

Requirements
Must have
• - simple flyer, the design is based on my logo. Brief information about my offer, reference to my homepage www.wegeimwandel-beratung.
- 2-sided: on the first page - fire circle with text (see homepage - Home), on the back - offer with logo
- possibly a square flyer

Should not have
• no photos

```html
<!DOCTYPE html>
<html lang="de">
<head>
<meta charset="utf-8">
<title>Wege im Wandel – Flyer</title>
<link rel="stylesheet" href="https://fonts.googleapis.com/css2?family=Bebas+Neue&family=Open+Sans:wght@300;400;600&display=swap">
<style>
  :root {
    --stage: #6e6f73;
    --gold: #9c7b2f;
    --cream: #fff4c6;
    --paper: #ffffff;
    --ink: #1d1d1b;
    --ink-soft: #333333;
  }
  * { margin: 0; padding: 0; box-sizing: border-box; }
  html, body { width: 1200px; height: 661px; overflow: hidden; background: var(--stage); }
  .flyer-side {
    position: absolute;
    top: 90px;
    width: 494px;
    height: 494px;
    box-shadow: 4px 5px 8px rgba(0,0,0,0.35);
    background: var(--paper);
  }
  .flyer-side svg { display: block; width: 100%; height: 100%; }
  .front { left: 96px; }
  .back { left: 641px; }

  .display { font-family: "Bebas Neue", "Oswald", sans-serif; }
  .body-text { font-family: "Open Sans", Arial, sans-serif; }
  .lead { font-weight: 600; font-size: 26px; fill: var(--ink); }
  .lead-copy { font-weight: 300; font-size: 22px; fill: var(--ink); }
  .badge-text { font-size: 25px; fill: var(--cream); }
  .offer-heading { font-size: 31px; fill: var(--gold); }
  .offer-heading-light { font-size: 31px; fill: var(--gold); opacity: 0.9; }
  .offer-title { font-weight: 600; font-size: 21px; fill: var(--ink); }
  .offer-copy { font-weight: 400; font-size: 17.5px; fill: var(--ink-soft); }
  .brand-name { font-weight: 600; font-size: 30px; fill: var(--gold); }
  .brand-name-small { font-weight: 600; font-size: 25px; fill: var(--gold); }
  .call-to-action { font-size: 25px; fill: var(--cream); }
  .contact { font-weight: 400; font-size: 21px; fill: var(--cream); }
</style>
</head>
<body>

<section class="flyer-side front" aria-label="Vorderseite">
  <svg viewBox="0 0 800 800" xmlns="http://www.w3.org/2000/svg">
    <defs>
      <linearGradient id="front-paper" x1="0" y1="0" x2="1" y2="1">
        <stop offset="0" stop-color="#f7f7f7"/>
        <stop offset="1" stop-color="#e9e9e9"/>
      </linearGradient>
    </defs>
    <rect class="paper" width="800" height="800" fill="url(#front-paper)"/>
    <path class="thin-arc" d="M265,0 Q300,30 315,60" fill="none" stroke="var(--gold)" stroke-width="1.5"/>
    <path class="gold-field" d="M0,405 C150,290 420,330 520,470 C590,570 570,720 505,800 L0,800 Z" fill="var(--gold)"/>
    <path class="thin-arc" d="M0,485 Q70,495 125,490" fill="none" stroke="var(--cream)" stroke-width="1" opacity="0.7"/>
    <circle class="outline-ring" cx="400" cy="354" r="312" fill="none" stroke="var(--paper)" stroke-width="1.5"/>
    <circle class="cream-ring" cx="400" cy="354" r="294" fill="none" stroke="var(--cream)" stroke-width="20"/>
    <circle class="focus-circle" cx="400" cy="354" r="285" fill="var(--paper)"/>

    <text class="body-text lead" x="383" y="239" text-anchor="middle">Sie möchten</text>
    <text class="body-text lead-copy" x="385" y="280" text-anchor="middle">Ihre belastende Situation lösen.</text>
    <text class="body-text lead-copy" x="385" y="308" text-anchor="middle">Ihre wichtigen Fragen klären.</text>
    <text class="body-text lead" x="385" y="392" text-anchor="middle">leichter weiterkommen</text>
    <text class="body-text lead-copy" x="385" y="430" text-anchor="middle">in der frustrierenden Zusammenarbeit</text>
    <text class="body-text lead-copy" x="385" y="456" text-anchor="middle">oder Ihrem mühsamen (Zusammen-)Leben.</text>

    <circle class="badge" cx="655" cy="139" r="80" fill="var(--gold)"/>
    <text class="display badge-text" text-anchor="middle">
      <tspan x="655" y="118">IHRE</tspan>
      <tspan x="655" y="146">KOSTENFREIE</tspan>
      <tspan x="655" y="174">MEDIATION</tspan>
    </text>

    <g class="brand-mark">
      <circle cx="622" cy="718" r="32" fill="none" stroke="var(--gold)" stroke-width="3"/>
      <text class="body-text brand-name-small">
        <tspan x="666" y="712">Wege im</tspan>
        <tspan x="666" y="741">Wandel</tspan>
      </text>
    </g>
  </svg>
</section>

<section class="flyer-side back" aria-label="Rückseite">
  <svg viewBox="0 0 800 800" xmlns="http://www.w3.org/2000/svg">
    <rect class="paper" width="800" height="800" fill="var(--paper)"/>
    <path class="corner-accent" d="M710,0 L800,0 L800,80 C765,65 730,35 710,0 Z" fill="var(--cream)"/>

    <text class="display offer-heading" x="400" y="74" text-anchor="middle">ICH BEGLEITE SIE UND BRINGE IHNEN</text>
    <text class="display offer-heading-light" x="400" y="110" text-anchor="middle">ORIENTIERUNG, KLARHEIT UND UNTERSTÜTZUNG.</text>
    <line class="divider" x1="205" y1="136" x2="600" y2="136" stroke="var(--cream)" stroke-width="2"/>

    <text class="body-text offer-title" x="400" y="180" text-anchor="middle">Coaching</text>
    <text class="body-text offer-copy" x="400" y="205" text-anchor="middle">Manchmal braucht man ein Gegenüber zum Klären der eigenen Situation oder beim</text>
    <text class="body-text offer-copy" x="400" y="227" text-anchor="middle">Entdecken neuer Sichtweisen und Handlungsmöglichkeiten.</text>

    <text class="body-text offer-title" x="400" y="279" text-anchor="middle">Mediation</text>
    <text class="body-text offer-copy" x="400" y="304" text-anchor="middle">Gewisse Konflikte können Sie nicht mehr selber lösen. Wenige Worte entzünden einen</text>
    <text class="body-text offer-copy" x="400" y="325" text-anchor="middle">erbitterten Streit oder erzeugen eisige Stille.</text>

    <text class="body-text offer-title" x="400" y="377" text-anchor="middle">Begleitung von traumatisierten Menschen</text>
    <text class="body-text offer-copy" x="400" y="402" text-anchor="middle">Ihr Leben fühlt sich oft schwer, bedrückend und freudlos an. Erfolglos haben Sie probiert,</text>
    <text class="body-text offer-copy" x="400" y="424" text-anchor="middle">sich von dieser Kontakt- und Perspektivlosigkeit zu befreien.</text>

    <path class="cream-edge" d="M0,430 C150,620 320,640 400,635 C520,630 700,560 800,425" fill="none" stroke="var(--cream)" stroke-width="16"/>
    <path class="gold-field" d="M0,440 C150,632 320,650 400,645 C520,640 700,572 800,435 L800,800 L0,800 Z" fill="var(--gold)"/>
    <circle class="thin-arc" cx="40" cy="880" r="350" fill="none" stroke="var(--cream)" stroke-width="1" opacity="0.45"/>

    <g class="brand-mark">
      <circle cx="300" cy="519" r="38" fill="none" stroke="var(--gold)" stroke-width="3"/>
      <text class="body-text brand-name" x="350" y="530">Wege im Wandel</text>
    </g>

    <text class="display call-to-action" x="400" y="668" text-anchor="middle">BITTE ERKLÄREN SIE MIR IHR ANLIEGEN.</text>
    <text class="display call-to-action" x="400" y="697" text-anchor="middle">ZUR GENAUEREN BESPRECHUNG MELDE ICH MICH BEI IHNEN.</text>

    <g class="contact-row">
      <g class="icon-web" fill="none" stroke="var(--cream)" stroke-width="1.6">
        <circle cx="30" cy="760" r="9"/>
        <ellipse cx="30" cy="760" rx="4" ry="9"/>
        <line x1="21" y1="760" x2="39" y2="760"/>
      </g>
      <text class="body-text contact" x="46" y="767">wegeimwandel-beratung.ch</text>

      <g class="icon-phone">
        <circle cx="346" cy="760" r="9" fill="var(--cream)"/>
        <path d="M342,755 q1,-1 2,0 l1,2 q0,1 -1,2 q1,2 3,3 q1,-1 2,-1 l2,1 q1,1 0,2 q-2,2 -5,0 q-4,-3 -5,-6 q0,-2 1,-3 z" fill="var(--gold)"/>
      </g>
      <text class="body-text contact" x="362" y="767">078 412 56 90</text>

      <g class="icon-mail">
        <circle cx="530" cy="760" r="9" fill="var(--cream)"/>
        <rect x="524" y="756" width="12" height="8" fill="none" stroke="var(--gold)" stroke-width="1.3"/>
        <path d="M524,756 L530,761 L536,756" fill="none" stroke="var(--gold)" stroke-width="1.3"/>
      </g>
      <text class="body-text contact" x="546" y="767">info@wegeimwandel.ch</text>
    </g>
  </svg>
</section>

</body>
</html>
```